Souvenir and Health Food Products

We need a website designed for a Wholesaler & Distributor of Australia Made Souvenir & Health Food products. Our range includes many of Australia's leading brands: Willow's Cottage, Southern Meadow Essentials, Pebble & Ferne, Vanto Cosmetics, Drelona, K T Leathergoods, Trestin Leathergoods, Brekker's Salt & Tallowick Honey.

Design will be converted into a Dot Net Nuke skin and containers so needs to be compatible.

Needs to show off their products and be easy to navigate.

Would like a nice clean and corporate look.
Updates

Hi Everyone

All design concepts are with my client who has been extremely busy....hoping to get feedback from them this week.

Cheers
Mabel

Target Market(s)

Target market are retail shops looking to stock their products

Industry/Entity Type

Health

Number of Pages Required

2 pages

Requirements
Must have
• Proposed Site Map
• Home
• About Us
• Products
• Ordering
• Contact Us

• To be included in homepage design concept:

• Large area for a flash banner of rotating images on homepage
• Logo and Phone number in header for every page 07 5000 3172
• Some welcome text
• Some icons will need to be designed - Register for our newsletter and Contact Us
• Product category list on homepage – thumbnail image/name of category (click through)

• Product categories to use are:
• (allow for up to 15)
• • Willow’s Cottage (use p1000321/jpg)

• • Jojoba Oil (use TFP_0121.jpg))

• • Southern Meadow Essentials (use TFP_0077.jpg)

• Could you create a separate content page to show how products will look on category page with each product having a thumbnail image, description and Enquire now button.
Should not have
• No shopping cart or ecommerce needed

```html
<!DOCTYPE html>
<html lang="en">
<head>
<meta charset="utf-8">
<title>Marlow Trade Co – Wholesale Souvenir &amp; Health Food</title>
<link href="https://fonts.googleapis.com/css2?family=Arimo:wght@400;700&display=swap" rel="stylesheet">
<style>
:root{
  --orange:#ff9900;
  --orange-soft:#ffb84d;
  --orange-pale:#ffd28a;
  --peach:#fde3b8;
  --teal:#a9dcc8;
  --green:#1e8f2e;
  --page-bg:#ebebeb;
  --card-bg:#f7f7f7;
  --tile-bg:#efefef;
  --text:#333;
  --white:#fff;
}
*{box-sizing:border-box;margin:0;padding:0}
html,body{width:1200px;height:3086px;overflow:hidden}
body{background:var(--page-bg);font-family:"Arimo",Arial,sans-serif;color:var(--text);position:relative}
.site{position:absolute;left:48px;width:1092px;height:1303px;background:var(--card-bg);border-radius:0 34px 34px 34px;overflow:hidden}
.site--home{top:137px}
.site--category{top:1646px}
.header{position:absolute;left:0;top:0;width:100%;height:146px;background:var(--white)}
.header-tint-left{position:absolute;left:0;top:0;width:420px;height:146px;background:radial-gradient(ellipse 120% 140% at 0% 0%,transparent 55%,var(--peach) 70%,var(--orange-pale) 82%,rgba(169,220,200,.7) 90%,transparent 96%)}
.header-tint-right{position:absolute;right:0;top:0;width:330px;height:60px;background:linear-gradient(180deg,var(--orange-pale) 0%,var(--peach) 45%,transparent 100%);opacity:.8}
.brand{position:absolute;left:20px;top:22px;display:flex;align-items:center;gap:8px;font-size:22px;font-weight:700;color:var(--text)}
.brand-dot{width:14px;height:14px;background:var(--green);border-radius:50%}
.call{position:absolute;right:29px;top:78px;font-size:29px;font-weight:700;color:var(--green)}
.nav{position:absolute;left:0;top:146px;width:100%;height:43px;background:linear-gradient(var(--orange),#ffa620)}
.nav a{position:absolute;top:0;height:43px;line-height:43px;width:124px;margin-left:-62px;text-align:center;color:var(--white);font-size:16px;text-decoration:none}
.nav a.active{background:var(--orange-soft);color:#222}
.crumbs{position:absolute;left:24px;top:208px;display:flex;align-items:center;gap:8px;font-size:13px;color:var(--orange)}
.crumbs .here{color:#222}
.banner{position:absolute;left:24px;top:245px;width:742px;height:275px;background:linear-gradient(100deg,#6cae3a 0%,#b9d98a 30%,#f1e2d4 55%,#f7f4ef 100%)}
.banner-cta{position:absolute;left:516px;top:448px;width:250px;height:72px;background:var(--green);color:var(--white);font-size:13px;display:flex;align-items:center;justify-content:center;gap:10px}
.newsletter{position:absolute;left:789px;top:247px;width:279px;height:199px;background:var(--orange);border-radius:4px;padding:20px 26px;color:var(--white)}
.newsletter h3{font-size:19px;font-weight:700;padding-bottom:14px;border-bottom:1px solid var(--orange-pale)}
.newsletter p{font-size:9px;margin-top:22px}
.newsletter .field{margin-top:6px;height:18px;background:var(--white)}
.newsletter .submit{position:absolute;right:28px;top:140px;background:#f2f2f2;border:1px solid #555;border-radius:3px;color:#222;font-size:12px;padding:5px 14px}
.newsletter .rule{position:absolute;left:26px;right:26px;bottom:20px;border-top:1px solid var(--orange-pale)}
.contact-box{position:absolute;background:var(--white);border:2px solid var(--orange-pale);display:flex;align-items:center;justify-content:center;gap:22px;color:var(--orange);font-size:25px}
.site--home .contact-box{left:789px;top:472px;width:279px;height:51px}
.section-title{position:absolute;font-size:29px;font-weight:400;color:var(--green)}
.category-tile{position:absolute;background:var(--tile-bg);padding:18px 20px}
.category-tile h4{font-size:23px;font-weight:400;color:var(--green);display:flex;justify-content:space-between;align-items:center;white-space:nowrap;gap:8px}
.category-tile h4.long{font-size:18px}
.category-tile h4 svg{flex:none}
.product-shot{position:absolute;border-radius:6px}
.shot-jars{background:radial-gradient(ellipse at center,#6e8f4f 0%,#d8d0b0 55%,transparent 75%)}
.shot-pack{background:radial-gradient(ellipse at center,#7d8f4c 0%,#cfc9a4 55%,transparent 75%)}
.shot-oil{background:linear-gradient(90deg,transparent 0%,#e8b52a 20%,#b01d32 45%,#d8a020 75%,transparent 100%)}
.welcome{position:absolute;left:26px;top:1003px;width:1040px;height:171px;border-left:4px solid var(--orange);padding:2px 0 0 28px;font-size:15.4px;line-height:26.5px;color:#222}
.footer{position:absolute;left:0;top:1222px;width:100%;height:81px;background:var(--orange);color:var(--white);font-size:11px;text-align:right;padding:14px 22px 0 0}
.footer .cur{color:#222}
.footer .copy{margin-top:18px}
.sidebar-list{position:absolute;left:24px;top:245px;width:273px;height:278px;background:var(--orange);color:var(--white)}
.sidebar-list h3{height:53px;line-height:53px;background:var(--orange-soft);text-align:center;font-size:19px;font-weight:400}
.sidebar-list ul{list-style:none;padding:24px 0 0 30px}
.sidebar-list li{font-size:18px;font-weight:700;margin-bottom:13px;display:flex;align-items:center;gap:14px;white-space:nowrap}
.sidebar-list li.long{font-size:14px;gap:10px}
.sidebar-list li::before{content:"";flex:none;width:9px;height:9px;background:var(--white)}
.sidebar-list li.active{color:var(--orange-pale);font-weight:400}
.site--category .contact-box{left:49px;top:484px;width:222px;height:36px;font-size:19px;border:none;gap:14px}
.side-tile{width:273px;height:206px;padding:14px 24px}
.side-tile h4{font-size:19px}
.side-tile h4.long{font-size:13.5px}
.cat-header{position:absolute;left:326px;top:247px;width:742px;height:87px;background:linear-gradient(var(--orange),var(--orange-soft));padding:16px 28px;font-size:42px;font-weight:400;color:var(--green)}
.cat-image{position:absolute;left:326px;top:334px;width:742px;height:120px;background:linear-gradient(90deg,#f6e7b2 0%,#e2b63a 35%,#f3e8c4 55%,#d7a72a 85%,#f0dfa5 100%)}
.product-grid{position:absolute;left:326px;top:459px;width:742px;height:736px;background:var(--tile-bg)}
.product-grid .divider{position:absolute;left:371px;top:20px;width:1px;height:700px;background:#aaa}
.product{position:absolute;width:300px;height:201px}
.product .shot-oil{left:0;top:0;width:154px;height:160px;position:absolute}
.product .info{position:absolute;left:177px;top:8px;font-size:14px;line-height:29px;color:#555}
.product .order{position:absolute;left:177px;top:112px;width:106px;height:38px;border:2px solid var(--green);border-radius:4px;background:var(--white);color:var(--green);font-size:16px;text-align:center;line-height:34px}
.product .sep{position:absolute;left:-2px;top:186px;width:290px;border-top:1px solid var(--orange-pale)}
</style>
</head>
<body>

<svg width="0" height="0" style="position:absolute">
  <defs>
    <symbol id="go" viewBox="0 0 40 40"><circle cx="20" cy="20" r="17" fill="none" stroke="currentColor" stroke-width="3"/><path d="M11 20h17M21 13l7 7-7 7" fill="none" stroke="currentColor" stroke-width="3" stroke-linecap="round" stroke-linejoin="round"/></symbol>
    <symbol id="home" viewBox="0 0 16 16"><path d="M2 8L8 2l6 6M4 7v7h8V7" fill="none" stroke="currentColor" stroke-width="1.6"/></symbol>
    <symbol id="mail" viewBox="0 0 36 24"><rect x="1" y="1" width="34" height="22" fill="var(--orange)"/><path d="M1 1l17 13L35 1" fill="none" stroke="#fff" stroke-width="2"/></symbol>
  </defs>
</svg>

<section class="site site--home">
  <header class="header">
    <div class="header-tint-left" role="img" aria-label="Soft orange and green header decoration"></div>
    <div class="header-tint-right" role="img" aria-label="Soft orange header decoration"></div>
    <div class="brand"><span class="brand-dot"></span>Marlow Trade Co</div>
    <div class="call">Call&nbsp; 07 5000 3172</div>
  </header>
  <nav class="nav">
    <a class="active" style="left:226px">Home</a>
    <a style="left:363px">About Us</a>
    <a style="left:511px">Products</a>
    <a style="left:658px">Ordering</a>
    <a style="left:813px">Contact Us</a>
  </nav>
  <div class="crumbs"><svg width="16" height="16"><use href="#home"/></svg>HOME</div>

  <div class="banner" role="img" aria-label="Rotating banner: woman with green leaves, natural skincare"></div>
  <div class="banner-cta">CHECK OUR NEW PRODUCTS <svg width="26" height="26" style="color:#fff"><use href="#go"/></svg></div>

  <form class="newsletter">
    <h3>Sign up for newsletter</h3>
    <p>* Please type in your email address</p>
    <div class="field"></div>
    <span class="submit">SUBMIT</span>
    <div class="rule"></div>
  </form>
  <div class="contact-box"><svg width="36" height="24"><use href="#mail"/></svg>CONTACT US</div>

  <h2 class="section-title" style="left:27px;top:555px">Product Category</h2>

  <div class="category-tile" style="left:24px;top:633px;width:333px;height:255px">
    <h4>Willow’s Cottage <svg width="42" height="42" style="color:var(--orange)"><use href="#go"/></svg></h4>
    <div class="product-shot shot-jars" style="left:50px;top:80px;width:240px;height:150px" role="img" aria-label="Willow’s Cottage jars and bottles"></div>
  </div>
  <div class="category-tile" style="left:381px;top:633px;width:333px;height:255px">
    <h4 class="long">Southern Meadow Essentials <svg width="42" height="42" style="color:var(--orange)"><use href="#go"/></svg></h4>
    <div class="product-shot shot-pack" style="left:100px;top:75px;width:140px;height:155px" role="img" aria-label="Southern Meadow Essentials soap packs"></div>
  </div>
  <div class="category-tile" style="left:735px;top:633px;width:333px;height:255px">
    <h4>Jojoba Oil <svg width="42" height="42" style="color:var(--orange)"><use href="#go"/></svg></h4>
    <div class="product-shot shot-oil" style="left:80px;top:70px;width:180px;height:160px" role="img" aria-label="Jojoba oil bottles and boxes"></div>
  </div>

  <h2 class="section-title" style="left:32px;top:918px">et iuquam ut</h2>
  <p class="welcome">Lorem ipsum dolor sit amet, consectetur adipiscing elit. Sed dictum mollis metus, sed varius leo convallis ac. Nulla id augue eu leo tristique consectetur et sit amet lectus. Cum sociis natoque penatibus et magnis dis parturient montes, nascetur ridiculus mus. Sed sed turpis ipsum. Curabitur ipsum velit, vestibulum id bibendum at, eleifend at diam. Quisque cursus tincidunt dignissim. Morbi semper bibendum nisi, blandit hendrerit ligula dictum et. Praesent gravida eros et leo pretium vel accumsan sem feugiat. Quisque vitae sapien vel tortor tempor consecte r sed eget felis. Proin lectus nisi, congue eget bibendum vitae, aliquam nec dolor. Aliquam porta enim vel sapien placerat condimentum. M ecenas consequat viverra dolor, ut tempus ligula varius at. Pellentesque gravida di</p>

  <footer class="footer">
    <div>| <span class="cur">Home</span> | About Us | Products | Ordering | Contact Us |</div>
    <div class="copy">Copyright @ Marlow Trade Co 2009</div>
  </footer>
</section>

<section class="site site--category">
  <header class="header">
    <div class="header-tint-left" role="img" aria-label="Soft orange and green header decoration"></div>
    <div class="header-tint-right" role="img" aria-label="Soft orange header decoration"></div>
    <div class="brand"><span class="brand-dot"></span>Marlow Trade Co</div>
    <div class="call">Call&nbsp; 07 5000 3172</div>
  </header>
  <nav class="nav">
    <a style="left:226px">Home</a>
    <a style="left:363px">About Us</a>
    <a class="active" style="left:511px;width:134px;margin-left:-67px">Products</a>
    <a style="left:658px">Ordering</a>
    <a style="left:813px">Contact Us</a>
  </nav>
  <div class="crumbs"><svg width="16" height="16"><use href="#home"/></svg>HOME | Products | <span class="here">Jojoba Oil</span></div>

  <aside class="sidebar-list">
    <h3>CATEGORY LIST</h3>
    <ul>
      <li class="active">Jojoba Oil</li>
      <li>Willow’s Cottage</li>
      <li class="long">Southern Meadow Essentials</li>
    </ul>
  </aside>
  <div class="contact-box"><svg width="28" height="19"><use href="#mail"/></svg>CONTACT US</div>

  <div class="category-tile side-tile" style="left:24px;top:548px">
    <h4 class="long">Southern Meadow Essentials <svg width="36" height="36" style="color:var(--orange)"><use href="#go"/></svg></h4>
    <div class="product-shot shot-pack" style="left:80px;top:60px;width:120px;height:130px" role="img" aria-label="Southern Meadow Essentials soap packs"></div>
  </div>
  <div class="category-tile side-tile" style="left:24px;top:787px">
    <h4>Willow’s Cottage <svg width="36" height="36" style="color:var(--orange)"><use href="#go"/></svg></h4>
    <div class="product-shot shot-jars" style="left:40px;top:60px;width:200px;height:130px" role="img" aria-label="Willow’s Cottage jars and bottles"></div>
  </div>

  <h1 class="cat-header">Jojoba Oil</h1>
  <div class="cat-image" role="img" aria-label="Close-up of golden jojoba oil bottles"></div>

  <div class="product-grid">
    <div class="divider"></div>
    <div class="product" style="left:52px;top:60px"><div class="shot-oil" role="img" aria-label="Jojoba oil product"></div><div class="info">Jojoba oil<br>ITEM: 25465<br>PRICE: $15.00</div><div class="order">ORDER</div><div class="sep"></div></div>
    <div class="product" style="left:412px;top:60px"><div class="shot-oil" role="img" aria-label="Jojoba oil product"></div><div class="info">Jojoba oil<br>ITEM: 25465<br>PRICE: $15.00</div><div class="order">ORDER</div><div class="sep"></div></div>
    <div class="product" style="left:52px;top:259px"><div class="shot-oil" role="img" aria-label="Jojoba oil product"></div><div class="info">Jojoba oil<br>ITEM: 25465<br>PRICE: $15.00</div><div class="order">ORDER</div><div class="sep"></div></div>
    <div class="product" style="left:412px;top:259px"><div class="shot-oil" role="img" aria-label="Jojoba oil product"></div><div class="info">Jojoba oil<br>ITEM: 25465<br>PRICE: $15.00</div><div class="order">ORDER</div><div class="sep"></div></div>
    <div class="product" style="left:52px;top:461px"><div class="shot-oil" role="img" aria-label="Jojoba oil product"></div><div class="info">Jojoba oil<br>ITEM: 25465<br>PRICE: $15.00</div><div class="order">ORDER</div></div>
    <div class="product" style="left:412px;top:461px"><div class="shot-oil" role="img" aria-label="Jojoba oil product"></div><div class="info">Jojoba oil<br>ITEM: 25465<br>PRICE: $15.00</div><div class="order">ORDER</div></div>
  </div>

  <footer class="footer">
    <div>| Home | About Us | <span class="cur">Products</span> | Ordering | Contact Us |</div>
    <div class="copy">Copyright @ Marlow Trade Co 2009</div>
  </footer>
</section>

</body>
</html>
```